Restricted Contest for Business Cards and Stationery
Restricted Contest for Business Cards and Stationery - Aviation
Use same font as used in my logo
Norman T. Whitby
President
40735 Cedar Hollow Lane Tampa, Florida 33418 U.S.A.
ntwhitby@corvanetrainers.com
www.corvanetrainers.com
Please create layouts for business cards, stationary and CD labels. Keep it clean and simple. I have uploaded two files. The file including the Peregrine Falcon Head, Wing and Lettering is our logo. Please consider using the second file, just the Peregrine Head, as a "water mark" for the letterhead. Please use a simple white background. Thank you.

```html
<!DOCTYPE html>
<html lang="en">
<head>
<meta charset="utf-8">
<title>Corvane Trainers — Stationery Set</title>
<link rel="stylesheet" href="https://fonts.googleapis.com/css2?family=Exo+2:ital,wght@0,700;1,400&family=Open+Sans:ital,wght@0,400;0,600;1,600&display=swap">
<style>
  :root {
    --backdrop: #b8823a;
    --paper: #ffffff;
    --navy: #1d2a55;
    --gold: #c99a3a;
    --ink: #3a3a3a;
    --ghost: #e9ebee;
    --flap-line: #d6d6d6;
  }
  * { margin: 0; padding: 0; box-sizing: border-box; }
  html, body { width: 1200px; height: 849px; overflow: hidden; }
  body { background: var(--backdrop); position: relative; font-family: "Open Sans", Arial, sans-serif; color: var(--ink); }

  .sheet { position: absolute; background: var(--paper); overflow: hidden; box-shadow: 0 1px 3px rgba(0,0,0,.25); }

  .brand { position: absolute; display: flex; align-items: center; gap: 4px; font-family: "Exo 2", Arial, sans-serif; font-weight: 700; color: var(--navy); text-transform: uppercase; letter-spacing: .02em; white-space: nowrap; }
  .brand-dot { border-radius: 50%; background: var(--navy); flex: none; }

  .stripe { position: absolute; right: 0; }
  .stripe-navy { background: var(--navy); }
  .stripe-gold { background: var(--gold); }

  .watermark { position: absolute; border-radius: 50% 50% 40% 60%; background: radial-gradient(ellipse at 40% 40%, #e2e5ea 0%, var(--ghost) 55%, rgba(233,235,238,0) 75%); }

  /* Business card */
  .business-card { left: 115px; top: 173px; width: 202px; height: 142px; }
  .business-card .brand { left: 12px; top: 18px; font-size: 11px; }
  .business-card .brand-dot { width: 8px; height: 8px; }
  .business-card .stripe-navy { left: 108px; top: 24px; height: 4px; }
  .business-card .stripe-gold { left: 108px; top: 29px; height: 2px; }
  .card-person { position: absolute; left: 0; right: 0; top: 44px; text-align: center; }
  .card-name { font-size: 6.5px; font-weight: 600; font-style: italic; color: var(--navy); }
  .card-role { font-size: 4.5px; margin-top: 1px; }
  .card-contact { position: absolute; left: 0; right: 0; top: 66px; text-align: center; font-size: 4.2px; line-height: 1.45; }
  .card-web { position: absolute; left: 0; right: 0; bottom: 12px; text-align: center; font-size: 5px; font-weight: 600; font-style: italic; color: var(--navy); }

  /* CD label */
  .cd-label { position: absolute; left: 57px; top: 501px; }
  .cd-brand { font-family: "Exo 2", Arial, sans-serif; font-weight: 700; font-size: 15px; fill: var(--navy); letter-spacing: .02em; }
  .cd-web { font-family: "Open Sans", Arial, sans-serif; font-weight: 600; font-style: italic; font-size: 7.5px; fill: var(--navy); }

  /* Letterhead */
  .letterhead { left: 461px; top: 185px; width: 348px; height: 574px; }
  .letterhead .brand { left: 20px; top: 40px; font-size: 13px; }
  .letterhead .brand-dot { width: 9px; height: 9px; }
  .letterhead .stripe-navy { left: 148px; top: 47px; height: 5px; }
  .letterhead .stripe-gold { left: 148px; top: 53px; height: 3px; }
  .letterhead .watermark { left: -30px; top: 280px; width: 200px; height: 250px; }
  .letter-footer { position: absolute; right: 26px; bottom: 28px; text-align: right; font-size: 4.4px; line-height: 1.5; }

  /* Envelope front */
  .envelope-front { left: 833px; top: 247px; width: 295px; height: 166px; }
  .envelope-front .brand { left: 10px; top: 14px; font-size: 10px; }
  .envelope-front .brand-dot { width: 7px; height: 7px; }
  .envelope-front .stripe-navy { left: 108px; top: 19px; height: 4px; }
  .envelope-front .stripe-gold { left: 108px; top: 24px; height: 2px; }
  .envelope-front .watermark { left: 8px; top: 40px; width: 130px; height: 120px; }

  /* Envelope back */
  .envelope-back { left: 833px; top: 427px; width: 295px; height: 168px; }
  .envelope-flap { position: absolute; inset: 0; }
  .return-address { position: absolute; right: 26px; bottom: 24px; text-align: right; font-size: 4.2px; line-height: 1.5; }
</style>
</head>
<body>

<section class="sheet business-card">
  <div class="brand"><span class="brand-dot"></span>Corvane</div>
  <div class="stripe stripe-navy"></div>
  <div class="stripe stripe-gold"></div>
  <div class="card-person">
    <p class="card-name">Norman T. Whitby</p>
    <p class="card-role">President</p>
  </div>
  <div class="card-contact">
    <p>40735 Cedar Hollow Lane</p>
    <p>Tampa, Florida 33418 U.S.A.</p>
    <p>Phone: +1 (813) 555-0148</p>
    <p>Email: ntwhitby@corvanetrainers.com</p>
  </div>
  <p class="card-web">www.corvanetrainers.com</p>
</section>

<svg class="cd-label" width="298" height="298" viewBox="0 0 298 298" aria-label="CD label">
  <defs>
    <clipPath id="disc-clip"><circle cx="149" cy="149" r="149"/></clipPath>
  </defs>
  <circle cx="149" cy="149" r="149" fill="#ffffff"/>
  <g clip-path="url(#disc-clip)">
    <ellipse cx="70" cy="95" rx="95" ry="100" fill="#eceef1" role="img" aria-label="Faint falcon head watermark"/>
    <rect x="150" y="131" width="160" height="11" fill="#1d2a55"/>
    <rect x="150" y="144" width="160" height="5" fill="#c99a3a"/>
  </g>
  <circle cx="28" cy="138" r="5" fill="#1d2a55"/>
  <text class="cd-brand" x="38" y="143">CORVANE</text>
  <circle cx="149" cy="149" r="25" fill="#b8823a"/>
  <circle cx="149" cy="149" r="25" fill="none" stroke="#e3e3e3" stroke-width="1"/>
  <text class="cd-web" x="178" y="170">www.corvanetrainers.com</text>
</svg>

<section class="sheet letterhead">
  <div class="watermark" role="img" aria-label="Faint falcon head watermark"></div>
  <div class="brand"><span class="brand-dot"></span>Corvane</div>
  <div class="stripe stripe-navy"></div>
  <div class="stripe stripe-gold"></div>
  <div class="letter-footer">
    <p>40735 Cedar Hollow Lane</p>
    <p>Tampa, Florida 33418 U.S.A.</p>
    <p>Phone: +1 (813) 555-0148</p>
    <p>www.corvanetrainers.com</p>
  </div>
</section>

<section class="sheet envelope-front">
  <div class="watermark" role="img" aria-label="Faint falcon head watermark"></div>
  <div class="brand"><span class="brand-dot"></span>Corvane</div>
  <div class="stripe stripe-navy"></div>
  <div class="stripe stripe-gold"></div>
</section>

<section class="sheet envelope-back">
  <svg class="envelope-flap" width="295" height="168" viewBox="0 0 295 168" aria-hidden="true">
    <polyline points="0,6 147,52 295,6" fill="none" stroke="#d6d6d6" stroke-width="1"/>
    <line x1="0" y1="6" x2="295" y2="6" stroke="#d6d6d6" stroke-width="1"/>
  </svg>
  <div class="return-address">
    <p>40735 Cedar Hollow Lane</p>
    <p>Tampa, Florida 33418 U.S.A.</p>
    <p>www.corvanetrainers.com</p>
  </div>
</section>

</body>
</html>
```